Shop window posters and banners for a contact lens (Carlow&Birkett Velora Pro)

Please take a look at our appearance on Instagram (optique_valmire), where you can also see the shop windows. In this case we would like to advertise a specific contact lens in the shop window. For this we need a poster and a banner. I can send you pictures of the lens. The poster banner should be filled with questions such as: Are you already wearing High Quality? Does your lens also have a blue filter? Feel good even after wearing it for a long time? Make an appointment with our vision experts!

Target Market(s)

Reach people who are dissatisfied with their contact lenses at the end of the day. For whom it may be important to protect their eyes from blue light.

Requirements
Must have
• correspond to the style of the store

```html
<!DOCTYPE html>
<html lang="en">
<head>
<meta charset="utf-8">
<title>Optique Valmire – Contact Lens Poster</title>
<link rel="stylesheet" href="https://fonts.googleapis.com/css2?family=Barlow+Condensed:wght@300;400;500;600;700&display=swap">
<style>
  :root {
    --stage: #5a5859;
    --navy: #22315f;
    --sky: #1a9fd6;
    --paper-top: #f1f6fa;
    --paper-bottom: #b9c7d8;
    --white: #ffffff;
  }
  html, body {
    margin: 0;
    width: 1067px;
    height: 1200px;
    overflow: hidden;
    background: var(--stage);
  }
  .poster {
    position: absolute;
    left: 183px;
    top: 128px;
    width: 1053px;
    height: 1418px;
    transform: scale(0.6667);
    transform-origin: top left;
    overflow: hidden;
    box-shadow: 6px 6px 8px rgba(0,0,0,0.35);
    background: linear-gradient(160deg, var(--paper-top) 0%, #dfe8f1 40%, #c9d6e4 70%, var(--paper-bottom) 100%);
    font-family: "Barlow Condensed", "Arial Narrow", sans-serif;
    color: var(--navy);
  }
  .lens-photo {
    position: absolute;
    left: 120px;
    top: 393px;
    width: 735px;
    height: 460px;
    border-radius: 50%;
    background: radial-gradient(ellipse at center, rgba(120,160,190,0.55) 0%, rgba(160,190,212,0.35) 45%, rgba(200,216,230,0) 72%);
  }
  .intro {
    position: absolute;
    left: 77px;
    top: 96px;
    margin: 0;
    font-weight: 300;
    font-size: 52px;
    line-height: 60px;
    letter-spacing: 0.6px;
  }
  .headline {
    position: absolute;
    left: 72px;
    top: 158px;
    margin: 0;
    font-weight: 600;
    font-size: 144px;
    line-height: 136px;
    letter-spacing: -2px;
  }
  .headline .accent { color: var(--sky); display: block; }
  .brand-name {
    position: absolute;
    left: 777px;
    top: 150px;
    width: 196px;
    margin: 0;
    text-align: center;
    font-weight: 600;
    font-size: 34px;
    line-height: 42px;
    letter-spacing: 4px;
    color: var(--navy);
  }
  .questions {
    position: absolute;
    right: 59px;
    top: 741px;
    text-align: right;
    font-weight: 400;
    font-size: 52px;
    line-height: 51px;
    margin: 0;
  }
  .questions .accent { color: var(--sky); font-weight: 600; }
  .questions p { margin: 0; }
  .questions .rule {
    width: 164px;
    height: 5px;
    background: var(--navy);
    margin: 14px 4px 18px auto;
  }
  .footer-band {
    position: absolute;
    left: 0;
    top: 1000px;
    width: 1053px;
    height: 418px;
  }
  .cta {
    position: absolute;
    left: 0;
    width: 1053px;
    top: 1059px;
    margin: 0;
    text-align: center;
    color: var(--white);
    font-weight: 400;
    font-size: 64px;
    line-height: 77px;
  }
  .cta .accent { color: var(--sky); font-weight: 600; }
  .contact {
    position: absolute;
    color: var(--white);
    text-align: center;
    font-size: 30px;
    font-weight: 400;
  }
  .contact-social { left: 55px; top: 1270px; width: 200px; }
  .contact-web { left: 780px; top: 1270px; width: 230px; }
  .contact-icon { display: block; margin: 0 auto 4px; }
  .call-pill {
    position: absolute;
    left: 420px;
    top: 1252px;
    width: 212px;
    height: 38px;
    border-radius: 19px;
    background: var(--sky);
    color: var(--white);
    display: flex;
    align-items: center;
    justify-content: center;
    gap: 4px;
    font-size: 34px;
    font-weight: 400;
  }
  .phone-number {
    position: absolute;
    left: 0;
    width: 1053px;
    top: 1296px;
    text-align: center;
    color: var(--white);
    font-weight: 600;
    font-size: 62px;
    line-height: 74px;
  }
</style>
</head>
<body>
  <main class="poster">
    <div class="lens-photo" role="img" aria-label="Photo of two clear contact lenses resting on a reflective light blue surface"></div>

    <p class="intro">ARE YOU ALREADY WEARING</p>
    <h1 class="headline">HIGH<span class="accent">QUALITY?</span></h1>

    <p class="brand-name">OPTIQUE<br>VALMIRE</p>

    <div class="questions">
      <p>DOES YOURLENS ALSO</p>
      <p>HAVE A <span class="accent">BLUE FILTER?</span></p>
      <div class="rule"></div>
      <p>FEEL GOOD EVEN AFTER</p>
      <p>WEARING IT <span class="accent">FOR A LONG TIME?</span></p>
    </div>

    <svg class="footer-band" viewBox="0 0 1053 418" preserveAspectRatio="none" aria-hidden="true">
      <path d="M0 113 Q526 -95 1053 113 L1053 418 L0 418 Z" fill="var(--navy)"/>
      <path d="M0 110 Q526 -98 1053 110" fill="none" stroke="var(--sky)" stroke-width="9"/>
    </svg>

    <p class="cta">MAKE AN <span class="accent">APPOINTMENT</span><br>WITH OUR VISION EXPERTS!</p>

    <div class="contact contact-social">
      <svg class="contact-icon" width="30" height="30" viewBox="0 0 30 30" aria-hidden="true"><circle cx="15" cy="15" r="12" fill="none" stroke="#fff" stroke-width="3"/></svg>
      optique_valmire
    </div>

    <div class="call-pill">
      <svg width="26" height="26" viewBox="0 0 24 24" aria-hidden="true"><path fill="#fff" d="M6.6 10.8a15.1 15.1 0 0 0 6.6 6.6l2.2-2.2a1 1 0 0 1 1-.25 11.4 11.4 0 0 0 3.6.57 1 1 0 0 1 1 1V20a1 1 0 0 1-1 1A17 17 0 0 1 3 4a1 1 0 0 1 1-1h3.5a1 1 0 0 1 1 1c0 1.25.2 2.45.57 3.57a1 1 0 0 1-.25 1z"/></svg>
      CALL US
    </div>
    <div class="phone-number">00352/618390</div>

    <div class="contact contact-web">
      <svg class="contact-icon" width="32" height="32" viewBox="0 0 32 32" aria-hidden="true" fill="none" stroke="#fff" stroke-width="2">
        <circle cx="16" cy="16" r="13"/><ellipse cx="16" cy="16" rx="6" ry="13"/>
        <line x1="3" y1="16" x2="29" y2="16"/><line x1="5" y1="9" x2="27" y2="9"/><line x1="5" y1="23" x2="27" y2="23"/>
      </svg>
      optiquevalmire.shop
    </div>
  </main>
</body>
</html>
```